We are looking for a clean new looking business card.

We would like a new, clean, and modern type business card with our updated contact information. We are a small a plumbing and heating and gasfitting company who offer 24 hr emergency service as well.
We feel our logo looks best on a white background.
Our current cards are outdated, both the design and the information.

Industry/Entity Type

Plumbing and heating

Contact Information for Business Card

Logo, Name, Title, Phone#, Email, Website, "24/7 Emergency Service"

Colors
0054AA
0677BA
7BADD7
CADEEF
E8F1F8

```html
<!DOCTYPE html>
<html lang="en">
<head>
<meta charset="utf-8">
<title>Northbrook Business Card</title>
<link rel="stylesheet" href="https://fonts.googleapis.com/css2?family=Open+Sans:wght@400;600;700&display=swap">
<style>
  :root {
    --bg: #3b3b3b;
    --card: #141414;
    --blue-deep: #0054aa;
    --blue: #0677ba;
    --blue-bright: #2f9ad8;
    --blue-light: #7badd7;
    --white: #f2f2f2;
    --emboss: #2a2a2a;
    --emboss-hi: #3c3c3c;
  }
  * { margin: 0; padding: 0; box-sizing: border-box; }
  html, body { width: 1200px; height: 801px; overflow: hidden; }
  body {
    background: var(--bg);
    font-family: "Open Sans", Arial, sans-serif;
    position: relative;
  }
  .card {
    position: absolute;
    width: 525px;
    height: 300px;
    background: var(--card);
    border-bottom: 3px solid var(--blue-bright);
    box-shadow: 0 14px 30px rgba(0,0,0,.45);
  }
  .card--front { left: 50px; top: 90px; }
  .card--back { left: 625px; top: 410px; }

  .brand {
    position: absolute;
    left: 28px; top: 96px;
    width: 230px;
    text-align: center;
  }
  .brand__mark {
    width: 34px; height: 34px;
    border-radius: 50%;
    background: var(--blue);
    margin: 0 auto 8px;
  }
  .brand__name {
    font-weight: 700;
    font-size: 40px;
    letter-spacing: 1px;
    line-height: 1;
    color: var(--blue-bright);
  }
  .brand__tagline {
    margin-top: 6px;
    font-size: 9.5px;
    font-weight: 600;
    letter-spacing: 2.4px;
    color: var(--white);
  }
  .divider {
    position: absolute;
    left: 280px; top: 40px;
    width: 1px; height: 150px;
    background: var(--blue-bright);
  }
  .contact {
    position: absolute;
    left: 300px; top: 44px;
    color: var(--white);
  }
  .contact__name {
    font-weight: 700;
    font-size: 19px;
    color: var(--blue-bright);
    letter-spacing: .3px;
  }
  .contact__title { font-size: 14px; margin-bottom: 14px; }
  .contact__line {
    display: flex; align-items: center; gap: 8px;
    font-size: 13px; line-height: 21px;
  }
  .contact__line svg { width: 11px; height: 11px; fill: var(--blue-bright); flex: none; }
  .emergency {
    position: absolute;
    left: 280px; right: 20px; bottom: 40px;
    text-align: center;
    color: var(--blue-bright);
    font-size: 15px;
    letter-spacing: .3px;
  }

  .back-brand {
    position: absolute;
    left: 0; right: 0; top: 78px;
    text-align: center;
  }
  .back-brand__mark {
    width: 52px; height: 52px;
    border-radius: 50%;
    background: var(--emboss);
    margin: 0 auto 10px;
  }
  .back-brand__name {
    font-weight: 700;
    font-size: 62px;
    line-height: 1;
    letter-spacing: 2px;
    color: var(--emboss-hi);
  }
  .back-brand__tagline {
    margin-top: 8px;
    font-size: 13px;
    font-weight: 600;
    letter-spacing: 3.4px;
    color: var(--emboss-hi);
  }
</style>
</head>
<body>
  <section class="card card--front">
    <div class="brand">
      <div class="brand__mark"></div>
      <div class="brand__name">northbrook</div>
      <div class="brand__tagline">PLUMBING · HEATING · GASFITTING</div>
    </div>
    <div class="divider"></div>
    <div class="contact">
      <div class="contact__name">DAN FERRELL</div>
      <div class="contact__title">President</div>
      <div class="contact__line">
        <svg viewBox="0 0 24 24"><path d="M6.6 10.8a15 15 0 0 0 6.6 6.6l2.2-2.2a1 1 0 0 1 1-.25 11.4 11.4 0 0 0 3.6.57 1 1 0 0 1 1 1V20a1 1 0 0 1-1 1A17 17 0 0 1 3 4a1 1 0 0 1 1-1h3.5a1 1 0 0 1 1 1c0 1.25.2 2.45.57 3.57a1 1 0 0 1-.25 1z"/></svg>
        555-014-2287
      </div>
      <div class="contact__line">
        <svg viewBox="0 0 24 24"><path d="M2 5h20v14H2z M2 5l10 8 10-8" /></svg>
        danf@northbrookpipe.com
      </div>
      <div class="contact__line">
        <svg viewBox="0 0 24 24"><circle cx="12" cy="12" r="10"/></svg>
        www.northbrookpipe.com
      </div>
    </div>
    <div class="emergency">"24/7 EMERGENCY SERVICE"</div>
  </section>

  <section class="card card--back">
    <div class="back-brand">
      <div class="back-brand__mark"></div>
      <div class="back-brand__name">northbrook</div>
      <div class="back-brand__tagline">PLUMBING · HEATING · GASFITTING</div>
    </div>
  </section>
</body>
</html>
```